Kestavo Estates is a commercial real estate development company based in the United States. We develop high-end office buildings and student housing apartments. We have a new logo and need to update all of our stationary items and business cards. We would like the design to be clean and professional. Our logo and color information is attached. Our logo MUST be in full color and not as white. It is preferred that the logo is on a white background.

Color code Blue R 0. G 62. B 124 ( #003E7C )
C 100 M84 Y 26 K 22
Black R32. G30. B30 ( #201E1E)
C100 M100 Y100 K100

Font used TRAJAN PRO3 PRO BOLD.

Items needed:
1. Business card - Leaning towards doing just a one side business card in a thicker paper. Include - logo, name - Peter T. Vance, Title - Chairman & CEO, 1870 Pembrook Blvd. Suite 400, Atlanta, GA 30127 - Cell number 404.555.####, Office 770.555.02## email@kestavoestates.com; www.kestavoestates.com.

2. Letterhead - Standard 8.5 by 11 paper. We do have a smaller size for the CEO that is 7.25 by 10.5 that is just a mirror of the letterhead except with his name (Peter T. Vance) and title (Chariman & CEO) listed at the top in the header. Letthead needs address, phone number and website, plus logo. *Prepared such that we can either implement as a Google Document template or professionally print.

3. Legal sized envelope - #10 envelope - which measures 4 1/8" by 9 1/2". We also use the same size envelope with a window. Need logo and address. A photo of the old envelope style is attached.

4. 9" x 12" Pocket folder - Need a design that can also be split to be a cover page and back - We use the cover pages in spiral binding machine, so we need to leave room on the left for that. One of the pockets should hold a business card. Include logo, address, phone, website. Also if text is needed, we could say development / leasing / property management.

5. Shipping label - 3 1/3" x 4" inches and 6 per page. Just need logo and address listed at top of the label and white space at bottom.

Company: Kestavo Estates
Address: 1870 Pembrook Blvd. Suite 400, Atlanta, GA 30127
Phone: 770.555.0214
Fax: 770.555.0287 (probably not needed)
Website: www.kestavoestates.com

Thank you for all your help!

Target Market(s)

Should communicate a strong corporate feel

Contact Information for Business Card

Include - logo, name - Peter T. Vance, Title - Chairman & CEO, 1870 Pembrook Blvd. Suite 400, Atlanta, GA 30127 - Cell number 404.555.####, Office 770.555.02## email@kestavoestates.com; www.kestavoestates.com.

Logo Text

Kestavo Estates

Colors

Requirements
Must have
• Our logo MUST be in full color and not as white. It is preferred that the logo is on a white background.
• Colors - Color code Blue R 0. G 62. B 124 ( #003E7C )
• C 100 M84 Y 26 K 22
Nice to have
• Font used in logo TRAJAN PRO3 PRO BOLD. Would love to see options of both a one sided and double-sided.
Should not have
• Logo in white.

```html
<!DOCTYPE html>
<html lang="en">
<head>
<meta charset="utf-8">
<title>Kestavo Estates Stationery</title>
<link rel="stylesheet" href="https://fonts.googleapis.com/css2?family=Cinzel:wght@700&family=Arimo:wght@400;700&family=Lato:wght@400&display=swap">
<style>
:root{
  --brand-blue:#003E7C;
  --ink:#201E1E;
  --body-grey:#6f6f6f;
  --paper:#f4f4f4;
  --card:#fbfbfb;
  --backdrop:#8a8580;
}
*{margin:0;padding:0;box-sizing:border-box}
html,body{width:1200px;height:1200px;overflow:hidden}
body{background:var(--backdrop);position:relative;font-family:"Arimo",Arial,sans-serif}

.wordmark{display:flex;align-items:center;gap:8px;color:var(--brand-blue);font-family:"Cinzel",serif;font-weight:700;white-space:nowrap}
.wordmark__dot{background:var(--brand-blue);border-radius:50%;flex:none}

.business-card{position:absolute;left:54px;width:304px;height:174px;background:var(--card);box-shadow:0 2px 6px rgba(0,0,0,.35)}
.business-card .wordmark{position:absolute;left:24px;top:24px;font-size:15px}
.business-card .wordmark__dot{width:20px;height:20px}
.business-card__tab{position:absolute;left:0;top:86px;width:5px;height:28px;background:var(--brand-blue);border-radius:0 4px 4px 0}
.business-card__name{position:absolute;left:24px;top:89px;font-family:"Cinzel",serif;font-weight:700;font-size:10px;color:var(--brand-blue)}
.business-card__title{position:absolute;left:24px;top:102px;font-family:"Lato",sans-serif;font-size:7px;color:var(--ink)}
.business-card__contacts{position:absolute;left:24px;top:126px;list-style:none;font-family:"Lato",sans-serif;font-size:7px;line-height:9px;color:var(--ink)}
.business-card__contacts li,.letterhead__contacts li{display:flex;align-items:center;gap:4px}
.business-card__address{position:absolute;right:24px;top:144px;text-align:right;font-family:"Lato",sans-serif;font-size:7px;line-height:9px;color:var(--ink)}
.icon{fill:none;stroke:var(--brand-blue);stroke-width:1.4;flex:none}

.letterhead{position:absolute;left:401px;top:122px;width:736px;height:953px;background:var(--paper);box-shadow:0 3px 10px rgba(0,0,0,.4)}
.letterhead .wordmark{position:absolute;left:50%;top:64px;transform:translateX(-50%);font-size:32px;gap:14px}
.letterhead .wordmark__dot{width:44px;height:44px}
.letter{position:absolute;left:86px;top:192px;width:580px;color:var(--body-grey);font-size:12px;line-height:16.8px}
.letter__date{margin-bottom:18px}
.letter__recipient strong,.letter__sign strong{font-weight:700}
.letter__salutation{margin-top:34px;margin-bottom:16px}
.letter p.letter__body{margin-bottom:16.8px;text-align:left}
.letter__closing{margin-top:26px}
.letter__signature{width:256px;height:38px;margin:2px 0 6px -10px;background:linear-gradient(90deg,rgba(32,30,30,.18),rgba(32,30,30,.05))}
.letterhead__contacts{position:absolute;left:52px;top:866px;list-style:none;font-family:"Lato",sans-serif;font-size:12px;line-height:14.5px;color:var(--ink)}
.letterhead__address{position:absolute;right:50px;top:895px;text-align:right;font-family:"Lato",sans-serif;font-size:12px;line-height:14.5px;color:var(--ink)}
.letterhead__band{position:absolute;left:0;bottom:0;width:100%;height:10px;background:var(--brand-blue)}
</style>
</head>
<body>

<section class="business-card" style="top:136px">
  <div class="wordmark"><span class="wordmark__dot"></span>KESTAVO ESTATES</div>
  <span class="business-card__tab"></span>
  <div class="business-card__name">PETER T. VANCE</div>
  <div class="business-card__title">Chairman &amp; CEO</div>
  <ul class="business-card__contacts">
    <li><svg class="icon" width="6" height="7" viewBox="0 0 6 7"><rect x="1" y="0.5" width="4" height="6" rx="0.6"/></svg>404.555.####</li>
    <li><svg class="icon" width="6" height="7" viewBox="0 0 6 7"><path d="M1 1 Q1 6 5 6"/></svg>770.555.02##</li>
    <li><svg class="icon" width="6" height="7" viewBox="0 0 6 7"><rect x="0.5" y="1.5" width="5" height="4"/><path d="M0.5 1.5 L3 4 L5.5 1.5"/></svg>email@kestavoestates.com</li>
    <li><svg class="icon" width="6" height="7" viewBox="0 0 6 7"><circle cx="3" cy="3.5" r="2.5"/></svg>www.kestavoestates.com</li>
  </ul>
  <div class="business-card__address">1870 Pembrook Blvd.<br>Suite 400, Atlanta, GA 30127</div>
</section>

<section class="business-card" style="top:336px">
  <div class="wordmark"><span class="wordmark__dot"></span>KESTAVO ESTATES</div>
  <span class="business-card__tab"></span>
  <div class="business-card__name">PETER T. VANCE</div>
  <div class="business-card__title">Chairman &amp; CEO</div>
  <ul class="business-card__contacts">
    <li><svg class="icon" width="6" height="7" viewBox="0 0 6 7"><rect x="1" y="0.5" width="4" height="6" rx="0.6"/></svg>404.555.####</li>
    <li><svg class="icon" width="6" height="7" viewBox="0 0 6 7"><path d="M1 1 Q1 6 5 6"/></svg>770.555.02##</li>
    <li><svg class="icon" width="6" height="7" viewBox="0 0 6 7"><rect x="0.5" y="1.5" width="5" height="4"/><path d="M0.5 1.5 L3 4 L5.5 1.5"/></svg>email@kestavoestates.com</li>
    <li><svg class="icon" width="6" height="7" viewBox="0 0 6 7"><circle cx="3" cy="3.5" r="2.5"/></svg>www.kestavoestates.com</li>
  </ul>
  <div class="business-card__address">1870 Pembrook Blvd.<br>Suite 400, Atlanta, GA 30127</div>
</section>

<section class="letterhead">
  <div class="wordmark"><span class="wordmark__dot"></span>KESTAVO ESTATES</div>
  <div class="letter">
    <div class="letter__date">January 1, 2050</div>
    <div class="letter__recipient"><strong>Daniel Reyes</strong><br>Managing Director<br>Co.Street, Building/Suite<br>City/State, Zip Code</div>
    <div class="letter__salutation">Dear Laura Whitcombe,</div>
    <p class="letter__body">Lorem ipsum dolor sit amet, consectetuer adipiscing elit, sed diam nonummy nibh euismod tincidunt ut laoreet dolore magna aliquam erat volutpat. Ut wisi enim ad minim veniam, quis nostrud exerci tation ullamcorper suscipit lobortis nisl ut aliquip ex ea commodo consequat. Duis dolore te feugait nulla facilisi. Nam liber tempor cum soluta nobis eleifend option congue nihil imperdiet doming id quod mazim placerat facer possim assum. Lorem ipsum dolor sit amet, consectetuer adipiscing elit, sed diam nonummy nibh euismod tincidunt ut laoreet dolore magna aliquam erat volutpat. Ut wisi enim ad minim veniam, quis nostrud exerci tation ullamcorper suscipit lobortis nisl ut aliquip ex ea commodo consequat.</p>
    <p class="letter__body">Consectetuer adipiscing elit, sed diam nonummy nibh euismod tincidunt ut laoreet dolore magna aliquam erat volutpat. Ut wisi enim ad minim veniam, quis nostrud exerci tation ullamcorper suscipit lobortis nisl ut aliquip ex ea commodo consequat. Consectetuer adipiscing elit, sed diam nonummy nibh euismod tincidunt ut laoreet dolore magna aliquam erat volutpat. Ut wisi enim ad minim veniam, quis nostrud exerci tation ullamcorper suscipit lobortis nisl ut aliquip ex ea commodo consequat.</p>
    <p class="letter__body">Duis dolore te feugait nulla facilisi. Nam liber tempor cum soluta nobis eleifend option congue nihil imperdiet doming id quod mazim placerat facer possim assum.Duis dolore te feugait nulla facilisi. Nam liber tempor cum soluta nobis eleifend option congue nihil imperdiet doming id quod mazim placerat facer possim assum.</p>
    <div class="letter__closing">Sincerely Yours,</div>
    <div class="letter__signature" role="img" aria-label="Handwritten signature of Marcus Ellery"></div>
    <div class="letter__sign"><strong>Authorized Managing Director</strong><br>Company Name Here</div>
  </div>
  <ul class="letterhead__contacts">
    <li><svg class="icon" width="10" height="11" viewBox="0 0 10 11"><rect x="2" y="1" width="6" height="9" rx="1"/></svg>404.555.####</li>
    <li><svg class="icon" width="10" height="11" viewBox="0 0 10 11"><path d="M2 2 Q2 9 8 9"/></svg>770.555.02##</li>
    <li><svg class="icon" width="10" height="11" viewBox="0 0 10 11"><rect x="1" y="2.5" width="8" height="6"/><path d="M1 2.5 L5 6 L9 2.5"/></svg>email@kestavoestates.com</li>
    <li><svg class="icon" width="10" height="11" viewBox="0 0 10 11"><circle cx="5" cy="5.5" r="4"/><path d="M1 5.5 H9 M5 1.5 V9.5"/></svg>www.kestavoestates.com</li>
  </ul>
  <div class="letterhead__address">1870 Pembrook Blvd.<br>Suite 400, Atlanta, GA 30127</div>
  <div class="letterhead__band"></div>
</section>

</body>
</html>
```